I need to design a business card
on the front side the words "VELTRIS CAPITAL" with the top half surrounded by a stylised cloud. Minimalist, navy blue font on white background, with the Veltris capital in embossing.

On the back contact details (avoid centered). I would rather have the details taking the 2/3rd on the right and having the logo on the left, but anyway not plain centered

Marcello Lo Ruffo
CEO e Fondatore

m.loruffo@veltris-capital.example
+39.328.514.6082

Piazza Ventrano 7
20135 Milano

```html
<!DOCTYPE html>
<html lang="it">
<head>
<meta charset="utf-8">
<title>Veltris Capital – Biglietto da visita</title>
<link rel="stylesheet" href="https://fonts.googleapis.com/css2?family=Crimson+Pro:wght@400;600&display=swap">
<style>
  :root {
    --backdrop: #e6e5e2;
    --card: #f7f7f5;
    --navy: #1c2a3c;
    --navy-soft: #3a4656;
    --shadow: rgba(40, 40, 40, 0.18);
  }
  * { box-sizing: border-box; margin: 0; padding: 0; }
  html, body {
    width: 1200px;
    height: 801px;
    overflow: hidden;
    background: var(--backdrop);
    font-family: "Crimson Pro", Georgia, serif;
    color: var(--navy);
  }
  .sheet {
    width: 1200px;
    height: 801px;
    display: flex;
    align-items: center;
    justify-content: center;
    gap: 40px;
  }
  .card {
    width: 520px;
    height: 336px;
    background: var(--card);
    box-shadow: 0 10px 24px var(--shadow), 0 1px 3px var(--shadow);
    position: relative;
  }
  .card--front {
    display: flex;
    align-items: center;
    justify-content: center;
  }
  .brand-name {
    font-weight: 400;
    font-size: 30px;
    letter-spacing: 0.32em;
    color: var(--navy);
    text-shadow: none;
    white-space: nowrap;
  }
  .card--front .brand-name { padding-left: 0.32em; }
  .card--back {
    display: grid;
    grid-template-columns: 1fr 2fr;
    align-items: center;
    padding: 0 36px 0 30px;
  }
  .card--back .brand-name {
    font-size: 15px;
    letter-spacing: 0.26em;
    white-space: normal;
    line-height: 1.6;
  }
  .contact { padding-left: 22px; }
  .contact__name {
    font-weight: 600;
    font-size: 22px;
    line-height: 1.1;
  }
  .contact__role {
    font-size: 17px;
    color: var(--navy-soft);
    margin-bottom: 18px;
  }
  .contact__line {
    font-size: 15px;
    line-height: 1.45;
  }
  .contact__label {
    font-weight: 600;
    display: inline-block;
    width: 16px;
  }
  .contact__address {
    margin-top: 16px;
    font-size: 15px;
    line-height: 1.45;
    color: var(--navy-soft);
  }
</style>
</head>
<body>
  <main class="sheet">
    <section class="card card--front" aria-label="Fronte">
      <p class="brand-name">VELTRIS CAPITAL</p>
    </section>

    <section class="card card--back" aria-label="Retro">
      <p class="brand-name">VELTRIS CAPITAL</p>
      <div class="contact">
        <p class="contact__name">Marcello Lo Ruffo</p>
        <p class="contact__role">CEO e Fondatore</p>
        <p class="contact__line"><span class="contact__label">e.</span> m.loruffo@veltris-capital.example</p>
        <p class="contact__line"><span class="contact__label">p.</span> +39.328.514.6082</p>
        <p class="contact__address">Piazza Ventrano 7<br>20135 Milano</p>
      </div>
    </section>
  </main>
</body>
</html>
```